"Oral Surgery Office needs a Business Card Design with Logo"

We need a logo design and business card. The name of the office is Tassingford Oral Surgery & Implant Center. The final design should communicate uniqueness as well as highly class office. The business card should emphasize power. I included the current business card below. Please design something unique

Target Market(s)

Dentists & Patients

Industry/Entity Type

Dental

Contact Information for Business Card

Unique Design to show success, prestige, Style, unmatched performance

Font styles to use
Serif

Colors
1b1b1b
ffffff
0556a4

Requirements
Must have
• Bussiness Name, Doctor's Name, Website, phone and Fax, email, office address
• Color should be either Black and White or Blue and White
Nice to have
• Clean look
Should not have
• the business card shouldn't be too busy. I feel like the old business card was too busy

```html
<!DOCTYPE html>
<html lang="en">
<head>
<meta charset="utf-8">
<title>Tassingford Oral Surgery &amp; Implant Center – Business Card</title>
<link href="https://fonts.googleapis.com/css2?family=Montserrat:wght@800&display=swap" rel="stylesheet">
<style>
  :root {
    --stage: #979697;
    --brand-blue: #0556a4;
    --paper: #ffffff;
    --ink: #1b1b1b;
    --photo-light: #e2e2e2;
    --photo-mid: #9a9a9a;
    --photo-dark: #3c3c3c;
  }
  * { margin: 0; padding: 0; box-sizing: border-box; }
  html, body { width: 1200px; height: 1000px; overflow: hidden; }
  body {
    background: var(--stage);
    font-family: "Montserrat", Arial, sans-serif;
    position: relative;
  }
  .card {
    position: absolute;
    left: 285px;
    width: 642px;
    height: 417px;
    overflow: hidden;
    box-shadow: 0 1px 4px rgba(0,0,0,0.35);
    background: var(--brand-blue);
  }
  .card--front { top: 43px; }
  .card--back { top: 494px; }

  .doctor-name {
    position: absolute;
    left: 22px;
    top: 24px;
    color: var(--paper);
    font-weight: 800;
    font-size: 22px;
    letter-spacing: 5.6px;
    text-transform: uppercase;
    white-space: nowrap;
  }
  .office-mark {
    position: absolute;
    right: 22px;
    top: 96px;
    display: flex;
    align-items: center;
    gap: 10px;
    color: var(--paper);
    font-weight: 800;
    font-size: 17px;
    letter-spacing: 3px;
    text-transform: uppercase;
  }
  .office-mark__square {
    width: 20px;
    height: 20px;
    background: var(--paper);
    flex: none;
  }
  .contact-list {
    position: absolute;
    left: 22px;
    top: 195px;
    list-style: none;
    color: var(--paper);
    font-weight: 800;
    font-size: 13.5px;
    line-height: 21.5px;
    letter-spacing: 3.2px;
    text-transform: uppercase;
    white-space: nowrap;
  }
  .name-strip {
    position: absolute;
    left: 0;
    bottom: 0;
    width: 100%;
    height: 76px;
    display: flex;
    align-items: center;
    padding-left: 22px;
    font-weight: 800;
    font-size: 17px;
    letter-spacing: 3.4px;
    text-transform: uppercase;
    white-space: nowrap;
  }
  .name-strip--light { background: var(--paper); color: var(--brand-blue); }
  .name-strip--blue { background: var(--brand-blue); color: var(--paper); padding-left: 25px; }

  .skyline-photo {
    position: absolute;
    left: 0;
    top: 0;
    width: 100%;
    height: 341px;
    background: linear-gradient(180deg, var(--photo-light) 0%, #cfcfcf 22%, var(--photo-mid) 40%, #7a7a7a 65%, var(--photo-dark) 100%);
  }
</style>
</head>
<body>
  <section class="card card--front">
    <h1 class="doctor-name">Dr. Marlen Veshtov</h1>
    <div class="office-mark"><span class="office-mark__square"></span><span>Tassingford</span></div>
    <ul class="contact-list">
      <li>2208 Harrow Lane</li>
      <li>Tassingford, NY 11490</li>
      <li>Tel: (555) 214 - 3900</li>
      <li>Fax: (555) 214 - 3906</li>
      <li>tassingfordsurgeon@mail.com</li>
      <li>www.tassingfordoralsurgery.com</li>
    </ul>
    <div class="name-strip name-strip--light">Tassingford Oral Surgery &amp; Implant Center</div>
  </section>

  <section class="card card--back">
    <div class="skyline-photo" role="img" aria-label="Black and white aerial photograph of a dense city skyline with tall towers"></div>
    <div class="name-strip name-strip--blue">Tassingford Oral Surgery &amp; Implant Center</div>
  </section>
</body>
</html>
```